Venlow Vaults -responsive, bootstrap website design

Looking to build a responsive service website.

Logo and pictures have been provided.

PLEASE REVIEW ATTACHED DESIGN STYLE GUIDES & CLIENT CREATIVE BRIEF FOR OUR REQUIREMENT. THANK YOU AND GOOD LUCK!
Updates

Industry/Entity Type

Build

```html
<!DOCTYPE html>
<html lang="en">
<head>
<meta charset="utf-8">
<title>Venlow Vaults</title>
<link href="https://fonts.googleapis.com/css2?family=Open+Sans:wght@400;600&family=Roboto+Condensed:wght@300;400&display=swap" rel="stylesheet">
<style>
:root{
  --red:#b4141b;
  --red-dark:#9c0f15;
  --ink:#555;
  --ink-soft:#777;
  --line:#e3e3e3;
  --band:#f3f3f3;
  --foot:#f2f2f2;
  --bar:#3d4450;
  --white:#fff;
}
*{margin:0;padding:0;box-sizing:border-box}
html,body{width:764px;height:1200px;overflow:hidden;background:var(--white)}
body{position:relative;font-family:"Open Sans",Arial,sans-serif;color:var(--ink)}
.abs{position:absolute}
.brand{left:32px;top:14px;width:136px;height:104px;border:2px solid #333;border-radius:8px;display:flex;align-items:center;justify-content:center;font-family:"Open Sans",Arial,sans-serif;font-weight:600;font-size:17px;color:#222}
.search{left:344px;top:50px;width:174px;height:32px;background:#f5f5f5;border:1px solid var(--line);font-size:10px;color:#999;padding:0 10px;display:flex;align-items:center;justify-content:space-between}
.cart{left:558px;top:50px;width:173px;height:32px;background:var(--red);color:var(--white);display:flex;align-items:center;padding:0 10px;font-size:11px;font-style:italic;gap:10px}
.cart b{font-weight:600}
.cart .caret{margin-left:auto;width:0;height:0;border:4px solid transparent;border-top-color:var(--white);margin-top:4px}
.nav{left:32px;top:134px;width:699px;height:44px;border:1px solid var(--line);border-bottom:none;display:flex}
.nav a{display:flex;align-items:center;justify-content:center;border-right:1px solid var(--line);font-size:13px;color:#555;text-decoration:none}
.nav a:last-child{border-right:none}
.nav a.active{color:var(--red);font-weight:600}
.hero{left:0;top:178px;width:764px;height:342px;background:radial-gradient(ellipse at 45% 45%,#7a0c0e 0%,#3c0506 45%,#0b0101 100%)}
.hero-art{left:280px;top:178px;width:484px;height:342px;background:radial-gradient(ellipse at 60% 55%,rgba(90,90,150,.35),rgba(60,120,40,.15) 50%,transparent 75%)}
.hero-title{left:30px;top:220px;font-family:"Roboto Condensed",Arial,sans-serif;font-weight:300;color:var(--white);line-height:1}
.hero-title .big{font-size:80px;letter-spacing:-1px}
.hero-title .mid{font-size:48px;margin-top:10px;letter-spacing:-1px}
.hero-copy{left:32px;top:380px;color:var(--white);font-size:14px;line-height:21px}
.hero-btn{left:32px;top:445px;width:56px;height:21px;background:var(--red);color:var(--white);font-size:9px;font-weight:600;display:flex;align-items:center;justify-content:center;font-family:Georgia,serif}
.band{left:0;top:520px;width:764px;height:84px;background:var(--band)}
.promo{top:547px;width:334px;height:114px;display:flex;align-items:center;font-family:"Roboto Condensed",Arial,sans-serif;color:var(--white)}
.promo-shop{left:33px;background:linear-gradient(90deg,#3a1d10,#6b3a1e 50%,#a35a25)}
.promo-pure{left:398px;background:linear-gradient(90deg,#3a0f10,#5b2a22 50%,#2a1212);justify-content:center;text-align:center}
.promo-shop .txt{margin-left:28px;font-size:33px;font-weight:300;line-height:37px}
.promo-shop .ico{position:absolute;left:246px;top:26px;width:61px;height:61px;background:var(--red);display:flex;align-items:center;justify-content:center}
.promo-pure .txt{line-height:1}
.promo-pure .l1{font-size:34px;font-weight:400;font-style:italic}
.promo-pure .l2{font-size:20px;font-weight:300;margin-top:4px}
.section-title{left:32px;top:693px;font-size:18px;color:var(--red);letter-spacing:.3px}
.rule{left:32px;top:731px;width:699px;height:1px;background:var(--line)}
.zoom{left:32px;top:775px}
.product{top:756px;width:127px}
.product .shot{margin-left:40px;width:40px;height:132px;border-radius:6px 6px 4px 4px;background:linear-gradient(180deg,#6b1620 0%,#1b1b1b 20%,#111 100%)}
.product .price{margin-top:10px;font-size:16px;color:var(--red)}
.product .name{margin-top:8px;font-size:12px;color:var(--ink-soft)}
.product .btn{margin-top:13px;height:29px;border:1px solid var(--line);display:flex;align-items:center;font-size:10px;color:#444}
.product .btn i{width:30px;height:29px;margin:-1px 16px 0 -1px;background:#444;display:flex;align-items:center;justify-content:center}
.product .btn.on{color:var(--red)}
.product .btn.on i{background:var(--red)}
.foot{left:0;top:1008px;width:764px;height:146px;background:var(--foot)}
.col{top:1025px}
.col h4{font-size:11px;font-weight:400;color:var(--red);margin-bottom:7px}
.col li{list-style:none;font-size:9px;color:#666;line-height:19px}
.col li.on{color:var(--red)}
.contact-row{display:flex;gap:10px;font-size:9px;color:#666;line-height:14px;margin-bottom:8px;align-items:center}
.contact-row i{width:24px;height:22px;background:#555;flex:none;display:flex;align-items:center;justify-content:center}
.bar{left:0;top:1154px;width:764px;height:46px;background:var(--bar);color:#ddd;font-size:9px;display:flex;align-items:center;padding:0 32px}
.social{margin-left:auto;display:flex;gap:6px}
.social span{width:23px;height:23px;border-radius:50%;background:#8a8f98}
.social span:first-child{background:#3b5ba0}
</style>
</head>
<body>
<header>
  <div class="abs brand">Venlow Vaults</div>
  <div class="abs search">Search
    <svg width="16" height="16" viewBox="0 0 16 16"><circle cx="6.5" cy="6.5" r="4.5" fill="none" stroke="#b4141b" stroke-width="2.4"/><line x1="10" y1="10" x2="14.5" y2="14.5" stroke="#b4141b" stroke-width="2.6" stroke-linecap="round"/></svg>
  </div>
  <div class="abs cart">
    <svg width="22" height="18" viewBox="0 0 22 18"><path d="M1 7h20l-2 10H3z" fill="#fff"/><path d="M6 7l5-6 5 6" fill="none" stroke="#fff" stroke-width="1.6"/></svg>
    <span><b>Cart:</b> 0 ITEMS(S)-$0.00</span><span class="caret"></span>
  </div>
  <nav class="abs nav">
    <a class="active" style="width:107px">Home</a>
    <a style="width:102px">About Us</a>
    <a style="width:95px">Services</a>
    <a style="width:117px">Wines Shop</a>
    <a style="width:105px">Our Store</a>
    <a style="width:79px">News</a>
    <a style="width:94px">Contact Us</a>
  </nav>
</header>

<section>
  <div class="abs hero" role="img" aria-label="Dark red backdrop with falling confetti"></div>
  <div class="abs hero-art" role="img" aria-label="Wine bottle, glass of red wine and bunches of grapes"></div>
  <div class="abs hero-title"><div class="big">FAST</div><div class="mid">DELIVERY</div></div>
  <p class="abs hero-copy">Dovitae diam purus luctus facilisisulla<br>Psum eros tris tique</p>
  <div class="abs hero-btn">More Info</div>
</section>

<div class="abs band"></div>
<div class="abs promo promo-shop" role="img" aria-label="Wine barrels in a cellar">
  <div class="txt">SHOP AND<br>SAVE 10%</div>
  <div class="ico"><svg width="30" height="26" viewBox="0 0 30 26"><path d="M1 3h5l4 14h15l3-10H9" fill="none" stroke="#fff" stroke-width="3" stroke-linejoin="round"/><circle cx="12" cy="22" r="2.5" fill="#fff"/><circle cx="23" cy="22" r="2.5" fill="#fff"/></svg></div>
</div>
<div class="abs promo promo-pure" role="img" aria-label="Stacked wine bottles">
  <div class="txt"><div class="l1">100% PURE</div><div class="l2">ORGANICE GRAPHES</div></div>
</div>

<h2 class="abs section-title">FEATURE PRODUCT</h2>
<div class="abs rule"></div>
<svg class="abs zoom" width="17" height="17" viewBox="0 0 17 17"><circle cx="7" cy="7" r="5" fill="none" stroke="#aaa" stroke-width="2.4"/><line x1="11" y1="11" x2="15.5" y2="15.5" stroke="#aaa" stroke-width="2.8" stroke-linecap="round"/></svg>

<div class="abs product" style="left:32px">
  <div class="shot" role="img" aria-label="Bottle of red wine"></div>
  <div class="price">$330.99</div><div class="name">APERCE SIT CONSE</div>
  <div class="btn on"><i><svg width="16" height="14" viewBox="0 0 30 26"><path d="M1 3h5l4 14h15l3-10H9" fill="none" stroke="#fff" stroke-width="3"/><circle cx="12" cy="22" r="2.5" fill="#fff"/><circle cx="23" cy="22" r="2.5" fill="#fff"/></svg></i>ADD TO CART</div>
</div>
<div class="abs product" style="left:223px">
  <div class="shot" role="img" aria-label="Bottle of red wine"></div>
  <div class="price">$330.99</div><div class="name">APERCE SIT CONSE</div>
  <div class="btn"><i><svg width="16" height="14" viewBox="0 0 30 26"><path d="M1 3h5l4 14h15l3-10H9" fill="none" stroke="#fff" stroke-width="3"/><circle cx="12" cy="22" r="2.5" fill="#fff"/><circle cx="23" cy="22" r="2.5" fill="#fff"/></svg></i>ADD TO CART</div>
</div>
<div class="abs product" style="left:414px">
  <div class="shot" role="img" aria-label="Bottle of red wine"></div>
  <div class="price">$330.99</div><div class="name">APERCE SIT CONSE</div>
  <div class="btn"><i><svg width="16" height="14" viewBox="0 0 30 26"><path d="M1 3h5l4 14h15l3-10H9" fill="none" stroke="#fff" stroke-width="3"/><circle cx="12" cy="22" r="2.5" fill="#fff"/><circle cx="23" cy="22" r="2.5" fill="#fff"/></svg></i>ADD TO CART</div>
</div>
<div class="abs product" style="left:605px">
  <div class="shot" role="img" aria-label="Bottle of red wine"></div>
  <div class="price">$330.99</div><div class="name">APERCE SIT CONSE</div>
  <div class="btn"><i><svg width="16" height="14" viewBox="0 0 30 26"><path d="M1 3h5l4 14h15l3-10H9" fill="none" stroke="#fff" stroke-width="3"/><circle cx="12" cy="22" r="2.5" fill="#fff"/><circle cx="23" cy="22" r="2.5" fill="#fff"/></svg></i>ADD TO CART</div>
</div>

<footer>
  <div class="abs foot"></div>
  <div class="abs col" style="left:32px"><h4>INFORMATION</h4><ul><li class="on">Home</li><li>About Us</li><li>Wine</li><li>Store</li><li>News</li></ul></div>
  <div class="abs col" style="left:155px"><h4>CUSTOMER SERVICES</h4><ul><li>Services</li><li>Returns</li><li>Site Map</li><li>Contact Us</li></ul></div>
  <div class="abs col" style="left:317px"><h4>EXTRAS</h4><ul><li>Brands</li><li>Gift Vouchers</li><li>Affiliates</li><li>Specials</li></ul></div>
  <div class="abs col" style="left:433px"><h4>MY ACCOUNT</h4><ul><li>My Account</li><li>Order History</li><li>Wish List</li><li>Newsletter</li></ul></div>
  <div class="abs col" style="left:562px"><h4>CONTACT US</h4>
    <div class="contact-row"><i><svg width="14" height="13" viewBox="0 0 14 13"><path d="M1 7L7 1l6 6M3 6v6h8V6" fill="none" stroke="#fff" stroke-width="1.6"/></svg></i><span>I-250 Lorem ispum, washington<br>Loren ispum comdesrt</span></div>
    <div class="contact-row"><i><svg width="12" height="12" viewBox="0 0 12 12"><path d="M2 1l3 3-1.5 1.5a7 7 0 003 3L8 7l3 3-2 2C5 12 0 7 0 3z" fill="#fff"/></svg></i><span>0123 456 7890</span></div>
    <div class="contact-row"><i><svg width="14" height="11" viewBox="0 0 14 11"><rect x="1" y="1" width="12" height="9" fill="none" stroke="#fff" stroke-width="1.4"/><path d="M1 1l6 5 6-5" fill="none" stroke="#fff" stroke-width="1.4"/></svg></i><span>info@venlowvaults.com</span></div>
  </div>
  <div class="abs bar">Copyright © 2014 Venlow Vaults. All Rights Reserved.
    <div class="social"><span></span><span></span><span></span></div>
  </div>
</footer>
</body>
</html>
```